Tellwick Asset Management - Corporate Letter Head Project

Looking for a classy design based on our current logo. Please find current logo source file in files. With our color scheme.

Target Market(s)

We're an investment firm, the letterhead needs to look professional and attractive to clients.

Industry/Entity Type

Hedgefund

Colors
0054AA
0677BA
7BADD7
CADEEF
E8F1F8

Requirements
Must have
• Our logo, address, phone number, and email

```html
<!DOCTYPE html>
<html lang="en">
<head>
<meta charset="utf-8">
<title>Tellwick Asset Management – Letterhead</title>
<link href="https://fonts.googleapis.com/css2?family=Cinzel:wght@500&family=Figtree:wght@300;400;700&display=swap" rel="stylesheet">
<style>
  :root {
    --navy: #0b1149;
    --ink: #4a4a4a;
    --rule: #555555;
    --paper: #ffffff;
    --on-navy: #ffffff;
  }
  html, body { margin: 0; padding: 0; overflow: hidden; background: var(--paper); }
  .letterhead {
    position: relative;
    width: 848px; height: 1200px;
    box-sizing: border-box;
    border: 1px solid var(--navy);
    background: var(--paper);
    overflow: hidden;
    font-family: "Figtree", sans-serif;
  }
  .brand-tab {
    position: absolute; left: 313px; top: 0; width: 222px; height: 171px;
  }
  .brand-tab svg { position: absolute; inset: 0; }
  .brand-dot {
    position: absolute; left: 101px; top: 58px; width: 20px; height: 20px;
    border-radius: 50%; background: var(--on-navy);
  }
  .brand-name {
    position: absolute; left: 20px; right: 20px; top: 100px;
    margin: 0; text-align: center; color: var(--on-navy);
    font-family: "Figtree", sans-serif; font-weight: 400;
    font-size: 17px; line-height: 21px; letter-spacing: 0.3px;
  }
  .section-title {
    position: absolute; color: var(--navy);
    font-family: "Cinzel", serif; font-weight: 500;
    text-align: center; margin: 0;
  }
  .section-title svg { position: absolute; inset: 0; overflow: visible; }
  .section-title span { position: relative; display: block; }
  .title-one { left: 334px; top: 222px; width: 179px; height: 40px; font-size: 27px; line-height: 40px; letter-spacing: 1px; }
  .title-two { left: 145px; top: 625px; width: 557px; height: 66px; font-size: 24px; line-height: 27px; letter-spacing: 2.4px; padding-top: 7px; box-sizing: border-box; }
  .body-copy {
    position: absolute; left: 121px; width: 605px;
    color: var(--ink); font-weight: 300;
    font-size: 13.6px; line-height: 18.55px;
    text-align: justify; hyphens: auto;
  }
  .body-copy p { margin: 0 0 18.55px; }
  .copy-one { top: 274px; }
  .copy-two { top: 703px; }
  .footer-rule { position: absolute; left: 120px; top: 1112px; width: 608px; height: 8px; }
  .footer-contact {
    position: absolute; left: 0; right: 0; top: 1130px;
    text-align: center; color: var(--rule);
    font-size: 10.6px; letter-spacing: 0.7px; font-weight: 400;
  }
  .footer-contact b { font-weight: 700; }
  .footer-contact .sep { margin: 0 6px; }
</style>
</head>
<body>
<main class="letterhead">
  <header class="brand-tab">
    <svg width="222" height="171" viewBox="0 0 222 171"><polygon points="0,0 222,0 222,159 210,171 12,171 0,159" fill="#0b1149"/></svg>
    <div class="brand-dot"></div>
    <p class="brand-name">Tellwick Asset Management</p>
  </header>

  <h1 class="section-title title-one">
    <svg width="179" height="40"><polygon points="0.5,0.5 170.5,0.5 178.5,8.5 178.5,39.5 8.5,39.5 0.5,31.5" fill="none" stroke="#0b1149" stroke-width="1"/></svg>
    <span>Headline</span>
  </h1>

  <section class="body-copy copy-one">
    <p>Quia sit, quaessit, aut maximolores invello eveliam quatempe mod mos essumqu aessimagnam et percia quiaspitiis dia verumque volupit utatum quidersperis et optatesequi rehenis a nobis di ut veliamusam et, quis sam atem hit di nossit dolupta conse adit ut voluptatur, totaquid quodipsum dit, veles exceatiates et odiorepel est et volorer cimiliquam voluptae ra eost voluptatur ressimagnit quo comnimo luptur, velenda dem re, tem as consed magnis repeles et et ut enihilita sunti dem explique vollandebit, omniscient ut in rest lab ilis quis voluptatur, sum et exerem sitaspi cienimus num expeles citinitae nulluptassed elitas alit ommolorrum doluptation poresto ritaturion re voluptat veligenda eatempo reptae re preperrum ipsanis molorios modite dellit, soluptaspiti cum remque conse cus doloribea dolupta tecatur modia que perio blaboritat verum a volore magnis que nullanda volupta cum dis milia quia nos eosapellam corem eratur, suntus di quiscienecea culpa quam eumquam, aliquam rehendebit, sedis dolumqui atiossit doluptatur? Ibusape ribusdam venecernatis coriate mporem reius ea id ut quo incti opti aut unt voluptae pel incteseque net voluptis modis que non reici to tet, sedi con nam ipitiorum hit a nonsecae vel iderio. Cus denimus, ut dolenda sit quunt minum eate plaut vel magnam endaeca borumqui omnihilic tendisq uature etusandit que volorrum explique et maio et landi corem. Litatur, sundicate ommod esed quo etusdae dolor autem faci quam lam aut fugit excearc hitatur, comnimus accus nobis asit volores exero core eat assitii scidia qui ipsumquaest facitiustem alis earis del inis plam apiciumque sitatiusa suntur?</p>
  </section>

  <h2 class="section-title title-two">
    <svg width="557" height="66"><polygon points="0.5,0.5 548.5,0.5 556.5,8.5 556.5,65.5 8.5,65.5 0.5,57.5" fill="none" stroke="#0b1149" stroke-width="1"/></svg>
    <span>Lupta nest, sum nam aut occae<br>pera aperend itest</span>
  </h2>

  <section class="body-copy copy-two">
    <p>Ga. Aligentibus sunt a simet hiciati occuptat quodis dolut iur, apiendigname videbis pa ipsaeri busdaes volupti bearchicatis magnist vere, sumquo bearci veliquatiore ommodis cimenis eosapis vitio beatqua mendunt mi, con rerspis atianim illestis dolorese res dolorpor reptaspiti ut eos iunt labo. Uciis perspel lorepudipid mint fuga. Ut in conse dolor aut volo vella volorit iorpore stibustore plis aut haria ant derruptae elisi iliciame nonsecus ut officimpore soluptatio is dest, eveniasit id maione cum rehento tatiur as eveniet ea voluptias quae non repra que nusciam sapienis atet hil illat.</p>
    <p>Es dolupis volestiataes nonsecus modis deles namus santem vellatur, omniene molores ulparum quis volor alibus debis dolore natur sunt erernam quid mi, verfersperis que</p>
    <p>Torem reptissi quis quid ut ea consendebis molorerite pore sequamusdae velligniam rest, offici nis ipsam ium quati dici officid quo tetur resed quistisquiae nonsequiae repe sandaep errorrore et re officit erchitatis eum fugit, eium volorecessi blandam usapienducit iduciam fuga. Ut prem consent quiani intem iur sunt qui consecume quo deleniaernam nimi, te dolorionet ma quatur mo occum id exceprem faciantem haruptatiam ne laces es perum, eaqui delibus, ium earcillati untorum, nes eum ipsa conemporerum issi non nienit erundaepelit rae omnis aut lacculluptis eos arite sum ium et perovid estiatem ea velit autemporit explicia nesti aces dolo int ut. exceprem faciantem haruptatiam ne laces es perum, eaqui delibus, ium earcillati untorum, nes eum ipsa conemporerum issi non nienit. exceprem faciantem haruptatiam ne laces es perum, eaqui delibus, ium earcillati untorum, nes eum ipsa conemporerum issi non nienit erundaepelit rae omnis aut lacculluptis eos arite sum ium et perovid estiatem ea velit autemporit explicia nesti aces dolo int ut. erundaepelit rae omnis aut.</p>
  </section>

  <footer>
    <svg class="footer-rule" width="608" height="8" viewBox="0 0 608 8">
      <line x1="4" y1="4" x2="604" y2="4" stroke="#555" stroke-width="0.8"/>
      <circle cx="4" cy="4" r="2.6" fill="#333"/>
      <circle cx="604" cy="4" r="2.6" fill="#333"/>
    </svg>
    <div class="footer-contact">
      Streetname zip code<span class="sep">/</span><b>phone:</b> 012 555014<span class="sep">/</span><b>Email:</b> pr@tellwickassetmgt.com<span class="sep">/</span><b>www.tellwickassetmgt.com</b>
    </div>
  </footer>
</main>
</body>
</html>
```